Site for company producing and selling products for children's health

We need an appealing professional web site design and images for a brand new company producing and selling products focused on children’s health. The site will offer information to visitors on the company, the company’s products, and general resources related to children’s health. Additionally the site will offer e-commerce functionality to allow for ordering of the company’s products.
The content and navigation for the site will be generated by programming, such as php or asp, and therefore any images used in the navigation portions of the site should allow for HTML markup to be overlaid rather than having the text built into the image or graphic.
The design must include 2 layouts, one for the landing/home page that includes only top navigation, and an inner page layout that includes both top and left navigation.
The header area of the site should include a place for links to access the visitor’s cart and profile similar to the top sections of plumvat.com, tidelor.com, and keenmart.com.
The landing page of the site should include some type of “changing” image area where we can include multiple image files for rotation to visitors similar to what is seen at vorta.com or brisksip.com. The flash/animation mechanism does not need to be provided (although it would be a plus if it was) but the design must accommodate the space for it.
The company’s colors are Orange (FF9900) and Blue (0066FF) and the logo can be viewed at http://wonkibrook.com/logo.png
All CSS and markup provided must be display consistently in Internet Explorer 7+, FifeFox, Google Chrome, and Safari.
Incorporating social media links (facebook, twitter, etc.) is desirable.
Parents who are conscious of health risks associated with children's diets and consumer food products.
E-Commerce

```html
<!DOCTYPE html>
<html lang="en">
<head>
<meta charset="utf-8">
<title>wonkibrook — home</title>
<link rel="stylesheet" href="https://fonts.googleapis.com/css2?family=Arimo:wght@400;700&display=swap">
<style>
:root{
  --orange:#ff9900;
  --orange-btn:#ffa532;
  --blue:#0066ff;
  --band-blue:#3f80e4;
  --title-blue:#2f6ce8;
  --field-blue:#7aa7f0;
  --ink:#111;
  --text:#6f6f6f;
  --muted:#9a9a9a;
  --footer-text:#a3a3a3;
  --tab-bg:#f7f7f7;
  --page:#ffffff;
}
*{box-sizing:border-box;margin:0;padding:0}
html,body{width:1200px;height:1108px;overflow:hidden;background:var(--page)}
body{font-family:"Arimo",Arial,sans-serif;color:var(--text);position:relative}
a{color:inherit;text-decoration:none}
.abs{position:absolute}

.top-rule{left:44px;top:8px;width:1112px;height:4px;background:var(--orange)}
.account-bar{right:66px;top:32px;font-size:14px;color:#333;display:flex;gap:18px;align-items:center}
.account-bar .sep{color:#555}
.cart{display:flex;align-items:center;gap:6px}
.cart .items{margin-left:12px}

.brand{left:94px;top:46px;display:flex;align-items:center;gap:10px}
.brand-dot{width:26px;height:26px;border-radius:50%;background:var(--orange)}
.brand-name{font-size:32px;font-weight:700;color:var(--blue);letter-spacing:-.5px}

.main-nav{left:407px;top:120px;display:flex;gap:12px}
.main-nav a{display:block;height:36px;line-height:38px;text-align:center;font-size:17px;color:#222;background:var(--tab-bg);border:1px solid #e4e4e4;border-bottom:none;border-radius:3px 3px 0 0;box-shadow:0 -2px 6px rgba(0,0,0,.08)}

.hero{left:44px;top:156px;width:1112px;height:328px;background:var(--band-blue)}
.hero-rotator{left:6px;top:6px;width:685px;height:316px;background:linear-gradient(180deg,#4fa0ea 0%,#7cc0f4 55%,#b5d9f0 80%,#6f9a3a 92%,#4f7a2a 100%)}
.slogan{left:702px;top:12px;width:399px;height:152px;background:#eef3fb;border:2px solid #c9d6ea;padding:18px 34px}
.slogan h2{font-size:21px;color:var(--title-blue);font-weight:700;margin-bottom:16px}
.slogan p{font-size:14px;line-height:18px;color:var(--muted);width:276px}
.btn-orange{position:absolute;right:36px;bottom:18px;background:var(--orange-btn);color:#fff;font-size:14px;padding:5px 13px;border:1px solid #f0a040}

.newsletter{left:726px;top:176px;width:370px;height:140px;color:#fff}
.newsletter h2{position:absolute;left:0;top:0;font-size:21px;font-weight:700;white-space:nowrap}
.newsletter p{position:absolute;left:0;top:34px;font-size:14px;white-space:nowrap}
.field{position:absolute;left:0;display:flex;align-items:center;height:22px;font-size:13px}
.field.name{top:68px}
.field.email{top:104px}
.field label{width:58px}
.field span{display:block;width:188px;height:21px;background:var(--field-blue);border:1px solid #9dbcf2}
.btn-subscribe{position:absolute;left:268px;top:96px;height:28px;line-height:26px;background:#d6eaff;color:#5a7fb0;font-size:14px;padding:0 10px;border:1px solid #fff}

.fade-band{left:44px;top:484px;width:1112px;height:70px;background:linear-gradient(#ececec,#fff)}

.col-title{font-size:21px;font-weight:700;color:var(--title-blue)}
.service{top:573px;width:226px}
.service .col-title{margin-bottom:18px}
.service .photo{width:220px;height:88px}
.service h3{font-size:13px;color:var(--ink);margin:14px 0 12px}
.service p{font-size:13px;line-height:21px;width:220px}
.read-more{display:flex;justify-content:flex-end;align-items:center;gap:10px;color:var(--orange);font-size:13px;margin-top:14px}
.read-more svg{display:block}

.posts{left:641px;top:573px;width:505px}
.posts .col-title{margin-bottom:18px}
.post{display:flex;gap:24px}
.post .thumb{flex:none;width:94px;height:94px;background:linear-gradient(135deg,#c9a070,#7a5a3e 50%,#4c6fa8)}
.post h4{font-size:13px;color:var(--ink);margin-bottom:10px}
.post time{display:block;font-size:13px;color:#aaa;margin-bottom:6px}
.post p{font-size:13px;line-height:21px;width:382px}
.post-block + .post-block{margin-top:14px}
.post-block .read-more{margin-top:2px}

.footer-rule{left:44px;top:888px;width:1112px;height:4px;background:var(--orange)}
.foot-col{top:926px;font-size:13px;color:var(--footer-text)}
.foot-col h3{font-size:16px;font-weight:700;color:#999;margin-bottom:14px}
.foot-col li{list-style:none;display:flex;align-items:center;gap:12px;height:21px}
.contact-lines{top:964px;font-size:13px;color:var(--footer-text);line-height:21px}
.foot-brand{left:1010px;top:965px;display:flex;align-items:center;gap:8px}
.foot-brand .dot{width:18px;height:18px;border-radius:50%;background:#bdbdbd}
.foot-brand span{font-size:17px;font-weight:700;color:#bdbdbd}
.copyright{left:68px;top:1061px;font-size:13px;color:var(--footer-text)}
.foot-nav{left:349px;top:1061px;font-size:13px;color:var(--footer-text);display:flex;gap:14px}
.social{left:1005px;top:1055px;display:flex;gap:3px}
.social span{width:22px;height:22px;background:#bcbcbc;border-radius:2px}
.bottom-rule{left:0;top:1096px;width:1200px;height:12px;background:linear-gradient(#e3e3e3,#cfcfcf)}
</style>
</head>
<body>

<div class="abs top-rule"></div>

<nav class="abs account-bar" aria-label="Account">
  <a href="#">My Account</a><span class="sep">|</span>
  <a href="#">Order Status</a><span class="sep">|</span>
  <a href="#" class="cart">
    <svg width="18" height="16" viewBox="0 0 18 16" aria-hidden="true"><path d="M0 1h3l2.4 9h9.2L17 3.5H5" fill="none" stroke="#222" stroke-width="1.8"/><circle cx="6.5" cy="14" r="1.5" fill="#222"/><circle cx="13.5" cy="14" r="1.5" fill="#222"/></svg>
    Cart <span class="items">0 Items</span>
  </a>
</nav>

<a href="#" class="abs brand"><span class="brand-dot"></span><span class="brand-name">wonkibrook</span></a>

<nav class="abs main-nav" aria-label="Main">
  <a href="#" style="width:94px">Home</a>
  <a href="#" style="width:117px">About us</a>
  <a href="#" style="width:105px">News</a>
  <a href="#" style="width:117px">Products</a>
  <a href="#" style="width:117px">Services</a>
  <a href="#" style="width:107px">Contact</a>
</nav>

<section class="abs hero">
  <div class="abs hero-rotator" role="img" aria-label="Rotating banner photo: children jumping joyfully on grass under a blue sky"></div>
  <div class="abs slogan">
    <h2>Wonkibrook slogan goes here</h2>
    <p>Lorem ipsum dolor sit amet, consectetur adipiscing elit. Vivamus sit amet risus eu tellus consectetur</p>
    <a href="#" class="btn-orange">Read more</a>
  </div>
  <form class="abs newsletter">
    <h2>Subscribe to our Newsletter</h2>
    <p>Lorem ipsum dolor sit amet, consectetur adipiscing</p>
    <div class="field name"><label>Name</label><span></span></div>
    <div class="field email"><label>E-mail</label><span></span></div>
    <span class="btn-subscribe">Subscribe</span>
  </form>
</section>

<div class="abs fade-band"></div>

<article class="abs service" style="left:56px">
  <h2 class="col-title">Service title</h2>
  <div class="photo" role="img" aria-label="Photo: child blowing soap bubbles in a sunny garden" style="background:linear-gradient(135deg,#6f9a3c,#c6d38a 50%,#e7c7a0)"></div>
  <h3>Lorem ipsum dolar sit</h3>
  <p>Lorem ipsum dolor sit amet, consect-etur adipiscing elit. Vivamus sit amet risus eu tellus consectetur sceleris-que. Nunc scelerisque congue...</p>
  <a href="#" class="read-more">Read more <svg width="14" height="14" viewBox="0 0 14 14" aria-hidden="true"><circle cx="7" cy="7" r="6" fill="none" stroke="#ff9900" stroke-width="1.5"/><path d="M4 7h6M7.5 4.5 10 7l-2.5 2.5" fill="none" stroke="#ff9900" stroke-width="1.5"/></svg></a>
</article>

<article class="abs service" style="left:349px">
  <h2 class="col-title">Service title</h2>
  <div class="photo" role="img" aria-label="Photo: group of smiling children lying together" style="background:linear-gradient(135deg,#d8b594,#a87a58 50%,#e9d3bd)"></div>
  <h3>Lorem ipsum dolar sit</h3>
  <p>Lorem ipsum dolor sit amet, consect-etur adipiscing elit. Vivamus sit amet risus eu tellus consectetur sceleris-que. Nunc scelerisque congue ti...</p>
  <a href="#" class="read-more">Read more <svg width="14" height="14" viewBox="0 0 14 14" aria-hidden="true"><circle cx="7" cy="7" r="6" fill="none" stroke="#ff9900" stroke-width="1.5"/><path d="M4 7h6M7.5 4.5 10 7l-2.5 2.5" fill="none" stroke="#ff9900" stroke-width="1.5"/></svg></a>
</article>

<section class="abs posts">
  <h2 class="col-title">Recent Posts</h2>
  <div class="post-block">
    <div class="post">
      <div class="thumb" role="img" aria-label="Photo: children gathered around a computer"></div>
      <div><h4>Post title goes here</h4><time>18/8/2010</time><p>Lorem ipsum dolor sit amet, consectetur adipiscing elit. Viva-mus sit amet risus eu tellus consectetur scelerisque.</p></div>
    </div>
    <a href="#" class="read-more">Read more <svg width="14" height="14" viewBox="0 0 14 14" aria-hidden="true"><circle cx="7" cy="7" r="6" fill="none" stroke="#ff9900" stroke-width="1.5"/><path d="M4 7h6M7.5 4.5 10 7l-2.5 2.5" fill="none" stroke="#ff9900" stroke-width="1.5"/></svg></a>
  </div>
  <div class="post-block">
    <div class="post">
      <div class="thumb" role="img" aria-label="Photo: children gathered around a computer"></div>
      <div><h4>Post title goes here</h4><time>18/8/2010</time><p>Lorem ipsum dolor sit amet, consectetur adipiscing elit. Viva-mus sit amet risus eu tellus consectetur scelerisque.</p></div>
    </div>
    <a href="#" class="read-more">Read more <svg width="14" height="14" viewBox="0 0 14 14" aria-hidden="true"><circle cx="7" cy="7" r="6" fill="none" stroke="#ff9900" stroke-width="1.5"/><path d="M4 7h6M7.5 4.5 10 7l-2.5 2.5" fill="none" stroke="#ff9900" stroke-width="1.5"/></svg></a>
  </div>
</section>

<div class="abs footer-rule"></div>

<div class="abs foot-col" style="left:68px">
  <h3>Customer Service</h3>
  <ul>
    <li><svg width="9" height="8" viewBox="0 0 9 8" aria-hidden="true"><path d="M0 4h7M4.5 1.5 7 4 4.5 6.5" fill="none" stroke="#999" stroke-width="1.2"/></svg>Contact Us.</li>
    <li><svg width="9" height="8" viewBox="0 0 9 8" aria-hidden="true"><path d="M0 4h7M4.5 1.5 7 4 4.5 6.5" fill="none" stroke="#999" stroke-width="1.2"/></svg>Frequently Asked Questions.</li>
    <li><svg width="9" height="8" viewBox="0 0 9 8" aria-hidden="true"><path d="M0 4h7M4.5 1.5 7 4 4.5 6.5" fill="none" stroke="#999" stroke-width="1.2"/></svg>Return Policy Information.</li>
  </ul>
</div>
<div class="abs foot-col" style="left:349px;top:928px">
  <h3>My Account</h3>
  <ul>
    <li><svg width="9" height="8" viewBox="0 0 9 8" aria-hidden="true"><path d="M0 4h7M4.5 1.5 7 4 4.5 6.5" fill="none" stroke="#999" stroke-width="1.2"/></svg>Login/Register.</li>
    <li><svg width="9" height="8" viewBox="0 0 9 8" aria-hidden="true"><path d="M0 4h7M4.5 1.5 7 4 4.5 6.5" fill="none" stroke="#999" stroke-width="1.2"/></svg>My Account.</li>
    <li><svg width="9" height="8" viewBox="0 0 9 8" aria-hidden="true"><path d="M0 4h7M4.5 1.5 7 4 4.5 6.5" fill="none" stroke="#999" stroke-width="1.2"/></svg>Order Status</li>
  </ul>
</div>
<div class="abs contact-lines" style="left:641px">Phone: 000 000 000<br>Fax:&nbsp;&nbsp;&nbsp;&nbsp;&nbsp;&nbsp;000 000 000<br>info@wonkibrook.com</div>
<div class="abs contact-lines" style="left:852px">Address detals<br>Address details<br>Country</div>
<div class="abs foot-brand"><span class="dot"></span><span>wonkibrook</span></div>

<div class="abs copyright">© 2010 Copyright wonkibrook</div>
<nav class="abs foot-nav" aria-label="Footer">
  <a href="#">Home</a><span>|</span><a href="#">About us</a><span>|</span><a href="#">Services</a><span>|</span><a href="#">Products</a><span>|</span><a href="#">News</a><span>|</span><a href="#">Sitemap</a><span>|</span><a href="#">Contact us</a>
</nav>
<div class="abs social" aria-label="Social links"><span></span><span></span><span></span><span></span><span></span><span></span></div>

<div class="abs bottom-rule"></div>
</body>
</html>
```